Postcard Design

we are an environmentally safe cleaning company called Verdimop Services, that specializes in post construction cleanup. for example, rehabbed houses and newly built commercial or residential space. we would like this mailer directed at the construction companies in order for them to call us before the property is ready to go to the buyer/client. we would like to see designs including a wood grain background and various earth toned colors (something very crisp, clean and not "flashy" marketing). It is important to convey we have flexibly with scheduling, competitive pricing, and that cleaning these properties not only enhances the contractors work but provides them with a happy customer. we are also on porchly board with a A rating and provide a 100% satisfaction guarentee

Industry/Entity Type

Construction

```html
<!DOCTYPE html>
<html lang="en">
<head>
<meta charset="utf-8">
<title>Verdimop Services Postcard</title>
<link rel="stylesheet" href="https://fonts.googleapis.com/css2?family=Jost:wght@300;500;700&display=swap">
<style>
  :root {
    --leaf-light: #a9d373;
    --leaf-mid: #8cc152;
    --wood-dark: #5e3c20;
    --wood-mid: #8a5d36;
    --wood-edge: #6b4526;
    --card-green: #a3cf6c;
    --ink: #111111;
  }
  html, body {
    margin: 0;
    padding: 0;
    overflow: hidden;
    background: #ffffff;
  }
  .postcard {
    position: relative;
    width: 1200px;
    height: 929px;
    background: var(--card-green);
    font-family: "Jost", "Century Gothic", sans-serif;
    font-weight: 300;
    color: var(--ink);
    overflow: hidden;
  }
  .header-art {
    position: absolute;
    left: 0;
    top: 0;
    width: 1200px;
    height: 300px;
    display: block;
  }
  .brand-name {
    position: absolute;
    left: 45px;
    top: 112px;
    margin: 0;
    font-weight: 700;
    font-size: 104px;
    line-height: 1;
    letter-spacing: 1px;
  }
  .intro {
    position: absolute;
    left: 15px;
    top: 298px;
    width: 1170px;
    margin: 0;
    font-size: 28.5px;
    line-height: 42px;
  }
  .call-to-action {
    position: absolute;
    left: 0;
    top: 452px;
    width: 1200px;
    margin: 0;
    text-align: center;
    font-weight: 500;
    font-size: 28.5px;
    line-height: 42px;
  }
  .services-label {
    position: absolute;
    left: 52px;
    top: 524px;
    margin: 0;
    font-size: 28.5px;
    line-height: 42px;
  }
  .services-list {
    position: absolute;
    left: 370px;
    top: 524px;
    width: 400px;
    margin: 0;
    padding: 0;
    list-style: none;
    text-align: center;
    font-size: 28.5px;
    line-height: 45.5px;
  }
  .promise-list {
    position: absolute;
    left: 800px;
    top: 524px;
    width: 390px;
    margin: 0;
    padding: 0;
    list-style: none;
    font-size: 28.5px;
    line-height: 45.5px;
  }
  .promise-list li {
    display: flex;
    align-items: center;
    gap: 10px;
    white-space: nowrap;
  }
  .tick {
    flex: none;
    width: 22px;
    height: 22px;
  }
  .website-line {
    position: absolute;
    left: 0;
    top: 854px;
    width: 1200px;
    margin: 0;
    text-align: center;
    font-size: 28.5px;
    line-height: 42px;
  }
</style>
</head>
<body>
  <main class="postcard">
    <svg class="header-art" viewBox="0 0 1200 300" role="img" aria-label="Header artwork: wood grain band framed by a border of green leaves, with a cartoon broom beside the company name">
      <defs>
        <linearGradient id="leafBorder" x1="0" y1="0" x2="0" y2="1">
          <stop offset="0" stop-color="#a9d373"/>
          <stop offset="1" stop-color="#8cc152"/>
        </linearGradient>
        <linearGradient id="woodBand" x1="0" y1="0" x2="1" y2="0">
          <stop offset="0" stop-color="#6b4526"/>
          <stop offset="0.5" stop-color="#8a5d36"/>
          <stop offset="1" stop-color="#5e3c20"/>
        </linearGradient>
      </defs>
      <rect x="0" y="0" width="1200" height="300" fill="url(#leafBorder)"/>
      <rect x="0" y="45" width="1200" height="225" fill="url(#woodBand)"/>
    </svg>

    <h1 class="brand-name">Verdimop</h1>

    <p class="intro">Here at Verdimop Services we provide a enviromentally safe cleaning service for newly renovated buildings and new construction. We provide cleaning services that everyone can enjoy and take the weight off of your shoulders.</p>

    <p class="call-to-action">Contractors: call us before the property goes to your buyer.</p>

    <p class="services-label">services include:</p>
    <ul class="services-list">
      <li>Dusting</li>
      <li>Vaccuming</li>
      <li>Cleaning break area</li>
      <li>Bathrooms</li>
      <li>Take out trash/recycling</li>
      <li>plus many more</li>
    </ul>

    <ul class="promise-list">
      <li><svg class="tick" viewBox="0 0 22 22" aria-hidden="true"><path d="M3 11.5l5 5 11-11" fill="none" stroke="#111111" stroke-width="3" stroke-linecap="round" stroke-linejoin="round"/></svg>Flexible scheduling</li>
      <li><svg class="tick" viewBox="0 0 22 22" aria-hidden="true"><path d="M3 11.5l5 5 11-11" fill="none" stroke="#111111" stroke-width="3" stroke-linecap="round" stroke-linejoin="round"/></svg>Competitive pricing</li>
      <li><svg class="tick" viewBox="0 0 22 22" aria-hidden="true"><path d="M3 11.5l5 5 11-11" fill="none" stroke="#111111" stroke-width="3" stroke-linecap="round" stroke-linejoin="round"/></svg>A rating on porchly board</li>
      <li><svg class="tick" viewBox="0 0 22 22" aria-hidden="true"><path d="M3 11.5l5 5 11-11" fill="none" stroke="#111111" stroke-width="3" stroke-linecap="round" stroke-linejoin="round"/></svg>100% satisfaction</li>
      <li><svg class="tick" viewBox="0 0 22 22" aria-hidden="true" style="visibility:hidden"></svg>guarantee</li>
      <li><svg class="tick" viewBox="0 0 22 22" aria-hidden="true"><path d="M3 11.5l5 5 11-11" fill="none" stroke="#111111" stroke-width="3" stroke-linecap="round" stroke-linejoin="round"/></svg>Happy customers</li>
    </ul>

    <p class="website-line">Check out our website for a list of services at Verdimopservice.com</p>
  </main>
</body>
</html>
```